Eye Catching Business Card for Optometrist

We've recently refreshed our logo and now we need a fresh and bold look for our business cards. We provide progressive ways to improve people's vision and protect their eye health.

Use our new logo as guidance into the colors to use. As far as style goes, I love how bold and eye catching the card is for Lanternfly Studio. Feel free to use your creative judgement.

Tagline: "Seeing further, every single day."

pertinent info to include:

Dr. Martin Sowerby
Optometrist

2857 Bramwell Ridge Blvd #217
Larkfield, MO 63990
(555) 382-7190

marty@brightlenshomeoptics.example
www.brightlenshomeoptics.example

```html
<!DOCTYPE html>
<html lang="en">
<head>
<meta charset="utf-8">
<title>Brightlens Home Optics – Business Card</title>
<link rel="stylesheet" href="https://fonts.googleapis.com/css2?family=Open+Sans:ital,wght@0,400;0,600;0,800;1,400&display=swap">
<style>
  :root {
    --red: #e31e24;
    --brown: #5a4535;
    --tan: #d9bf99;
    --white: #ffffff;
    --ink: #4a4a4a;
    --stage: #e6e6e6;
  }
  * { box-sizing: border-box; margin: 0; padding: 0; }
  html, body { width: 1200px; height: 1200px; overflow: hidden; }
  body {
    background: var(--stage);
    font-family: "Open Sans", Arial, sans-serif;
    display: flex;
    flex-direction: column;
    align-items: center;
    justify-content: center;
    gap: 60px;
  }
  .card {
    position: relative;
    width: 560px;
    height: 320px;
    background: var(--white);
    overflow: hidden;
    box-shadow: 0 6px 18px rgba(0,0,0,0.12);
  }

  /* Front */
  .front .block { position: absolute; }
  .front .block-red { left: 0; top: 0; width: 230px; height: 110px; background: var(--red); }
  .front .block-tan { left: 230px; top: 60px; width: 60px; height: 50px; background: var(--tan); }
  .front .block-brown { left: 290px; top: 60px; width: 270px; height: 50px; background: var(--brown); }
  .front .accent-red { left: 0; top: 250px; width: 150px; height: 8px; background: var(--red); }
  .front .accent-tan { left: 150px; top: 250px; width: 50px; height: 22px; background: var(--tan); }
  .front .accent-brown { left: 200px; top: 272px; width: 360px; height: 48px; background: var(--brown); }
  .front .tagline {
    position: absolute; left: 40px; top: 140px;
    color: var(--red); font-size: 22px; font-weight: 400;
  }
  .front .brand {
    position: absolute; right: 36px; top: 196px;
    display: flex; align-items: center; gap: 10px;
  }

  .brand-square { width: 16px; height: 16px; background: var(--red); }
  .brand-name { color: var(--red); font-weight: 800; font-size: 20px; letter-spacing: 0.5px; text-transform: uppercase; }

  /* Back */
  .back .bar-red { position: absolute; left: 24px; top: 22px; width: 9px; height: 56px; background: var(--red); }
  .back .bar-brown { position: absolute; left: 24px; top: 232px; width: 9px; height: 66px; background: var(--brown); }
  .back .identity { position: absolute; left: 50px; top: 40px; }
  .back .doctor {
    color: var(--red); font-weight: 800; font-size: 19px;
    font-variant: small-caps; letter-spacing: 0.3px;
  }
  .back .role { color: var(--ink); font-size: 13px; margin-top: 2px; }
  .back .contacts { position: absolute; left: 50px; top: 116px; list-style: none; }
  .back .contacts li {
    display: flex; align-items: flex-start; gap: 8px;
    color: var(--ink); font-size: 13px; line-height: 17px;
  }
  .back .contacts li + li { margin-top: 1px; }
  .back .contacts svg { flex: none; width: 13px; height: 13px; margin-top: 2px; }
  .back .brand { position: absolute; right: 30px; bottom: 34px; display: flex; align-items: center; gap: 10px; }
</style>
</head>
<body>

  <section class="card front" aria-label="Card front">
    <div class="block block-red"></div>
    <div class="block block-tan"></div>
    <div class="block block-brown"></div>
    <div class="block accent-red"></div>
    <div class="block accent-tan"></div>
    <div class="block accent-brown"></div>
    <p class="tagline">"Seeing further, every single day."</p>
    <div class="brand">
      <span class="brand-square"></span>
      <span class="brand-name">Brightlens Home Optics</span>
    </div>
  </section>

  <section class="card back" aria-label="Card back">
    <div class="bar-red"></div>
    <div class="bar-brown"></div>
    <div class="identity">
      <h1 class="doctor">Dr. Martin Sowerby</h1>
      <p class="role">Optometrist</p>
    </div>
    <ul class="contacts">
      <li>
        <svg viewBox="0 0 13 13" aria-hidden="true"><circle cx="6.5" cy="6.5" r="6.5" fill="#5a4535"/><path d="M6.5 3a2.2 2.2 0 0 0-2.2 2.2c0 1.7 2.2 4.3 2.2 4.3s2.2-2.6 2.2-4.3A2.2 2.2 0 0 0 6.5 3z" fill="#fff"/></svg>
        <span>2857 Bramwell Ridge Blvd #217<br>Larkfield, MO 63990</span>
      </li>
      <li>
        <svg viewBox="0 0 13 13" aria-hidden="true"><circle cx="6.5" cy="6.5" r="6.5" fill="#5a4535"/><rect x="4.5" y="3" width="4" height="7" rx="0.8" fill="#fff"/></svg>
        <span>(555) 382-7190</span>
      </li>
      <li>
        <svg viewBox="0 0 13 13" aria-hidden="true"><circle cx="6.5" cy="6.5" r="6.5" fill="#5a4535"/><rect x="3.5" y="4.2" width="6" height="4.6" fill="#fff"/><path d="M3.5 4.2l3 2.4 3-2.4" stroke="#5a4535" stroke-width="0.7" fill="none"/></svg>
        <span>marty@brightlenshomeoptics.example</span>
      </li>
      <li>
        <svg viewBox="0 0 13 13" aria-hidden="true"><circle cx="6.5" cy="6.5" r="6.5" fill="#5a4535"/><circle cx="6.5" cy="6.5" r="3.3" stroke="#fff" stroke-width="0.8" fill="none"/><path d="M3.2 6.5h6.6M6.5 3.2c-1.6 2-1.6 4.6 0 6.6M6.5 3.2c1.6 2 1.6 4.6 0 6.6" stroke="#fff" stroke-width="0.7" fill="none"/></svg>
        <span>www.brightlenshomeoptics.example</span>
      </li>
    </ul>
    <div class="brand">
      <span class="brand-square"></span>
      <span class="brand-name">Brightlens Home Optics</span>
    </div>
  </section>

</body>
</html>
```